Harborline Motors LLC

Car Dealer Customer Service
Address: 2741 Linden Avenue, Shelbyville, TN 37162
web: www.harborlinemotorstn.net
email: harborlinemotorstn@mailbox-example.net
Phone: (931) 555-0148
Phone: (629) 555-0173

```html
<!DOCTYPE html>
<html lang="en">
<head>
<meta charset="utf-8">
<title>Harborline Motors – Business Card</title>
<link rel="stylesheet" href="https://fonts.googleapis.com/css2?family=Jost:wght@400;500;700&display=swap">
<style>
  :root {
    --stage: #e6e8e6;
    --card: #050505;
    --brand-blue: #2b86c5;
    --gold: #e8ac3a;
    --ink-light: #f2f2f2;
    --faint-blue: #0c1a26;
  }
  * { box-sizing: border-box; margin: 0; padding: 0; }
  html, body { width: 1200px; height: 900px; overflow: hidden; }
  body {
    background: var(--stage);
    font-family: "Jost", "Helvetica Neue", Arial, sans-serif;
    display: flex;
    flex-direction: column;
    align-items: center;
    justify-content: center;
    gap: 56px;
  }
  .card {
    position: relative;
    width: 630px;
    height: 360px;
    background: var(--card);
    overflow: hidden;
    box-shadow: 0 12px 30px rgba(0,0,0,0.25);
  }

  /* Contact side */
  .card--contact .backdrop-mark {
    position: absolute;
    right: -40px;
    top: -70px;
    width: 300px;
    height: 300px;
    border-radius: 50%;
    background: var(--faint-blue);
  }
  .brand-small {
    position: absolute;
    left: 56px;
    top: 52px;
    display: flex;
    align-items: center;
    gap: 12px;
  }
  .brand-small .brand-dot {
    width: 38px; height: 38px; border-radius: 50%;
    background: var(--brand-blue);
  }
  .brand-small .brand-name {
    color: var(--brand-blue);
    font-weight: 700;
    font-size: 17px;
    line-height: 1;
    letter-spacing: 0.02em;
    text-transform: uppercase;
  }
  .person {
    position: absolute;
    left: 56px;
    top: 132px;
  }
  .person-name {
    color: var(--gold);
    font-weight: 500;
    font-size: 26px;
    line-height: 1.1;
  }
  .person-role {
    color: var(--ink-light);
    font-size: 13px;
    margin-top: 2px;
  }
  .contact-list {
    position: absolute;
    left: 56px;
    bottom: 46px;
    list-style: none;
    color: var(--ink-light);
    font-size: 14px;
  }
  .contact-list li {
    display: flex;
    align-items: center;
    gap: 10px;
    line-height: 1.55;
  }
  .contact-list svg { width: 13px; height: 13px; fill: var(--gold); flex: none; }

  /* Logo side */
  .card--logo {
    display: flex;
    flex-direction: column;
    align-items: center;
    justify-content: center;
  }
  .brand-large { display: flex; flex-direction: column; align-items: center; }
  .brand-large .brand-dot {
    width: 110px; height: 110px; border-radius: 50%;
    background: var(--brand-blue);
    margin-bottom: 18px;
  }
  .brand-large .brand-name {
    color: var(--brand-blue);
    font-weight: 700;
    font-size: 44px;
    line-height: 1;
    letter-spacing: 0.01em;
    text-transform: uppercase;
  }
  .tagline {
    color: var(--ink-light);
    font-weight: 700;
    font-size: 17px;
    letter-spacing: 0.01em;
    margin-top: 6px;
    text-transform: uppercase;
  }
</style>
</head>
<body>

  <section class="card card--contact">
    <div class="backdrop-mark" aria-hidden="true"></div>

    <div class="brand-small">
      <span class="brand-dot" aria-hidden="true"></span>
      <span class="brand-name">Harborline Motors</span>
    </div>

    <div class="person">
      <p class="person-name">Person Name</p>
      <p class="person-role">Chief Executive</p>
    </div>

    <ul class="contact-list">
      <li>
        <svg viewBox="0 0 24 24" aria-hidden="true"><path d="M6.6 10.8a15.1 15.1 0 0 0 6.6 6.6l2.2-2.2a1 1 0 0 1 1-.25 11.4 11.4 0 0 0 3.6.57 1 1 0 0 1 1 1V20a1 1 0 0 1-1 1A17 17 0 0 1 3 4a1 1 0 0 1 1-1h3.5a1 1 0 0 1 1 1c0 1.25.2 2.45.57 3.6a1 1 0 0 1-.25 1z"/></svg>
        (931) 555-0148, (629) 555-0173
      </li>
      <li>
        <svg viewBox="0 0 24 24" aria-hidden="true"><path d="M12 2a10 10 0 1 0 0 20 10 10 0 0 0 0-20zm6.9 6h-3a15.7 15.7 0 0 0-1.4-3.6A8 8 0 0 1 18.9 8zM12 4c.8 1.2 1.5 2.5 1.9 4h-3.8c.4-1.5 1.1-2.8 1.9-4zM4.3 14a8 8 0 0 1 0-4h3.4a16 16 0 0 0 0 4zm.8 2h3a15.7 15.7 0 0 0 1.4 3.6A8 8 0 0 1 5.1 16zm3-8h-3a8 8 0 0 1 4.4-3.6C8.9 5.5 8.4 6.7 8.1 8zM12 20c-.8-1.2-1.5-2.5-1.9-4h3.8c-.4 1.5-1.1 2.8-1.9 4zm2.3-6H9.7a14.5 14.5 0 0 1 0-4h4.6a14.5 14.5 0 0 1 0 4zm.2 5.6c.6-1.1 1.1-2.3 1.4-3.6h3a8 8 0 0 1-4.4 3.6zm1.8-5.6a16 16 0 0 0 0-4h3.4a8 8 0 0 1 0 4z"/></svg>
        www.harborlinemotorstn.net
      </li>
      <li>
        <svg viewBox="0 0 24 24" aria-hidden="true"><path d="M2 5h20v14H2zm2 2v.5l8 5 8-5V7zm0 2.9V17h16V9.9l-8 5z"/></svg>
        harborlinemotorstn@mailbox-example.net
      </li>
      <li>
        <svg viewBox="0 0 24 24" aria-hidden="true"><path d="M12 2a7 7 0 0 0-7 7c0 5.2 7 13 7 13s7-7.8 7-13a7 7 0 0 0-7-7zm0 9.5A2.5 2.5 0 1 1 12 6.5a2.5 2.5 0 0 1 0 5z"/></svg>
        2741 Linden Avenue, Shelbyville, TN 37162
      </li>
    </ul>
  </section>

  <section class="card card--logo">
    <div class="brand-large">
      <span class="brand-dot" aria-hidden="true"></span>
      <span class="brand-name">Harborline Motors</span>
    </div>
    <p class="tagline">Car Dealer Customer Service</p>
  </section>

</body>
</html>
```